Website improvements and Adding Functionalities at https://vornet.site/pelmarq

1.Search functionality
2.Payment process functionality
3. Application configuration
4. Registration functionality activation
5. Chat functionality
6.Language switching functionality (Portuguese & French)
7.Bespoke interactive modules
8. Automated web scraping and data synchronisation mechanisms
9. News Page
10.Webinar facilities
11. Basic SEO optimisation
12. Speed and performance optimisation
13. Security configuration
14. Google Analytics integration
15. Cross-browser and mobile testing
16. Website deployment and launch support

Target Market(s)

My target markets are companies, investors, suppliers and professionals with an interest in the Mozambican oil and gas sector

Industry/Entity Type

Oil and Gas

Coding

Coded - Design and coding required

Number of Pages Required

1 page

Requirements
Must have
• Improve the existing page at https://vornet.site/pelmarq and add the following features to it: 1. Search functionality 2. Payment process functionality 3. Application configuration 4. Activation of registration functionality 5. Chat functionality 6. Language switching functionality (Portuguese & French) 7. Bespoke interactive modules 8. Automated web scraping and data synchronisation mechanisms 9. News Page

```html
<!DOCTYPE html>
<html lang="en">
<head>
<meta charset="utf-8">
<title>Pelmarq – Mozambique Oil &amp; Gas Intelligence</title>
<link href="https://fonts.googleapis.com/css2?family=Bebas+Neue&family=Roboto:wght@400;500;700&family=Lato:wght@400;700&display=swap" rel="stylesheet">
<style>
:root{
  --orange:#f0762d;
  --orange-light:#f79a3e;
  --navy:#1e1a3b;
  --purple:#2f2651;
  --text:#5c5c66;
  --light:#f3f2f5;
  --footer:#1b1930;
  --white:#fff;
}
*{margin:0;padding:0;box-sizing:border-box}
html,body{width:1200px;height:4191px;overflow:hidden;background:var(--white)}
body{font-family:"Lato",sans-serif;color:var(--text);position:relative}
section,header,footer{position:absolute;left:0;width:1200px}
.abs{position:absolute}
.display{font-family:"Bebas Neue",sans-serif;color:var(--navy);font-weight:400;letter-spacing:.5px}
.rule{width:78px;height:4px;background:var(--orange)}
.btn{display:inline-block;border-radius:22px;font-family:"Roboto",sans-serif;font-weight:700;font-size:13px;color:#fff;padding:0 15px;height:40px;line-height:40px;text-transform:uppercase;background:linear-gradient(180deg,var(--orange-light),var(--orange))}
.btn-dark{background:var(--navy)}
.brand-name{font-family:"Roboto",sans-serif;font-weight:700;color:var(--navy);letter-spacing:2px}
.tagline{font-family:"Roboto",sans-serif;font-weight:500;color:var(--orange);letter-spacing:3px}

/* header */
.site-header{top:0;height:110px;background:#fff;z-index:5}
.logo-cap{left:110px;top:0;width:270px;height:178px;background:#fff;border-radius:0 0 135px 135px;z-index:6;text-align:center}
.logo-dot{width:56px;height:56px;border-radius:50%;background:var(--navy);margin:14px auto 10px}
.logo-cap .brand-name{font-size:11px}
.logo-cap .tagline{font-size:7px;margin-top:4px}
.search{left:413px;top:22px;width:378px;height:32px;border:1px solid #ddd;border-radius:16px;font-size:11px;color:#777;padding:8px 20px}
.search svg{position:absolute;right:34px;top:7px}
.reg-top{left:860px;top:15px;height:40px;padding:0 15px}
.lang{left:1018px;top:24px;font-size:11px;color:#555;display:flex;gap:6px;align-items:center}
.nav{left:398px;top:78px;display:flex;gap:20px;font-family:"Roboto",sans-serif;font-size:13px;color:var(--navy)}
.nav .active{color:var(--orange);position:relative}
.nav .active:after{content:"";position:absolute;left:0;right:0;bottom:-14px;height:2px;background:var(--orange)}

/* hero */
.hero{top:110px;height:740px}
.hero-photo{position:absolute;inset:0;background:linear-gradient(100deg,#0f1c2e 0%,#1d3350 40%,#5a4a30 65%,#c9892f 82%,#2d4c6a 100%)}
.hero-curve{position:absolute;left:0;bottom:0}
.hero h1{left:113px;top:220px;font-size:66px;line-height:78px;color:#fff;white-space:nowrap}
.hero p{left:113px;top:460px;width:420px;font-family:"Roboto",sans-serif;font-weight:700;font-size:13px;line-height:27px;color:#fff}
.hero .btn{left:110px;top:582px}
.dots{left:578px;top:650px;display:flex;gap:8px}
.dots span{width:10px;height:10px;border-radius:50%;border:2px solid #fff}
.dots .on{background:var(--orange)}

/* about */
.about{top:850px;height:538px}
.about-photo{left:113px;top:60px;width:380px;height:380px;border-radius:50%;background:radial-gradient(circle at 60% 45%,#e0713a,#7c4a33 45%,#2b2a33 100%)}
.about h2{left:643px;top:80px;font-size:50px}
.about .rule{left:643px;top:137px}
.about .copy{left:643px;top:172px;width:450px;font-size:12.5px;line-height:22px}
.about .copy p+p{margin-top:10px}
.about .btn{left:643px;top:362px}

/* access */
.access{top:1388px;height:675px;background:linear-gradient(180deg,#2d2550,#3b3062 60%,#2c2449)}
.access h2{left:0;width:1200px;top:90px;text-align:center;color:#fff;font-size:52px}
.access .rule{left:561px;top:148px}
.card{top:232px;width:316px;height:363px;background:#fff;border-radius:158px 158px 0 0;text-align:center;padding-top:38px}
.card h3{font-family:"Roboto",sans-serif;font-weight:500;font-size:21px;line-height:31px;color:var(--navy);margin-top:26px}
.card p{font-size:14.5px;line-height:26px;margin:14px auto 0;width:230px}
.card-icon{width:92px;height:92px;border-radius:50%;background:var(--orange);margin:0 auto;display:flex;align-items:center;justify-content:center}
.card-feature{background:var(--orange);padding-top:12px}
.card-feature .ring{width:282px;height:282px;margin:0 auto;border-radius:50%;border:7px solid var(--navy);background:radial-gradient(circle,#e9edf5,#8a9cc0 55%,#3b4a72)}
.card-feature h3{color:#fff;font-weight:700;font-size:20px;margin-top:22px}
.arrow{top:444px;width:34px;height:34px;border-radius:50%;background:#fff;display:flex;align-items:center;justify-content:center}

/* unique */
.unique{top:2063px;height:745px}
.unique h2{left:111px;top:115px;font-size:50px}
.unique .rule{left:111px;top:184px}
.feature{left:111px;width:460px;display:flex;gap:30px}
.feature .ico{flex:none;width:77px;height:77px;border-radius:50%;border:2px solid var(--navy);display:flex;align-items:center;justify-content:center}
.feature h3{font-family:"Lato",sans-serif;font-weight:400;font-size:20px;color:var(--navy);margin-top:14px}
.feature p{font-size:15px;line-height:25px;margin-top:8px;width:340px}
.unique-photo{left:623px;top:155px;width:465px;height:465px;border-radius:50%;background:radial-gradient(circle at 50% 40%,#ffb24a,#e9652a 40%,#7a2f1c 80%,#3c1a14)}

/* how */
.how{top:2808px;height:485px;background:var(--light)}
.how-photo{left:0;top:0}
.how h2{left:650px;top:75px;font-size:52px}
.how .rule{left:650px;top:137px}
.how p{left:648px;top:175px;width:450px;font-family:"Roboto",sans-serif;font-size:12.5px;line-height:33.5px}
.how .btn{left:648px;top:366px}

/* cta */
.cta{top:3293px;height:470px;text-align:center}
.cta h2{left:0;width:1200px;top:90px;font-size:54px;line-height:58px}
.cta .rule{left:561px;top:227px}
.cta p{left:0;width:1200px;top:265px;font-family:"Roboto",sans-serif;font-size:16px;line-height:30px}
.cta .btns{left:0;width:1200px;top:343px;display:flex;justify-content:center;gap:10px}

/* footer */
.site-footer{top:3755px;height:436px;color:#fff}
.footer-bg{position:absolute;left:0;top:0}
.site-footer h4{font-family:"Roboto",sans-serif;font-weight:500;font-size:22px}
.links{left:110px;top:145px}
.links ul{list-style:none;margin-top:12px;font-family:"Roboto",sans-serif;font-size:11px;line-height:23px;padding-left:4px}
.foot-brand{left:400px;top:120px;width:400px;text-align:center}
.foot-brand .logo-dot{width:80px;height:80px;background:var(--orange);margin:0 auto 14px}
.foot-brand .brand-name{color:#fff;font-size:12px}
.foot-brand .tagline{font-size:10px;margin-top:6px}
.social{display:flex;gap:14px;justify-content:center;margin-top:22px}
.social span{width:31px;height:31px;border-radius:50%;border:2px solid #fff}
.contact{left:847px;top:145px}
.contact ul{list-style:none;margin-top:18px;font-family:"Roboto",sans-serif;font-size:11px;line-height:17px}
.contact li{display:flex;gap:18px;margin-bottom:20px;width:260px}
.contact svg{flex:none}
.foot-line{left:110px;top:403px;width:940px;height:1px;background:#55536a}
.copyright{left:0;width:1200px;top:413px;text-align:center;font-family:"Roboto",sans-serif;font-size:11px}
.chat{left:1045px;top:370px;width:53px;height:53px;border-radius:50%;background:var(--orange);border:3px solid #fff;display:flex;align-items:center;justify-content:center}
</style>
</head>
<body>

<header class="site-header">
  <div class="abs logo-cap">
    <div class="logo-dot"></div>
    <div class="brand-name">PELMARQ CO</div>
    <div class="tagline">LINKING TALENT. DRIVING OUTCOMES.</div>
  </div>
  <div class="abs search">Search here...
    <svg width="16" height="16" viewBox="0 0 16 16"><circle cx="6.5" cy="6.5" r="5" fill="none" stroke="#888" stroke-width="1.5"/><path d="M10.5 10.5l4 4" stroke="#888" stroke-width="1.5"/></svg>
  </div>
  <a class="abs btn reg-top">Register Now</a>
  <div class="abs lang">
    <svg width="18" height="18" viewBox="0 0 18 18" fill="none" stroke="#666" stroke-width="1.2"><circle cx="9" cy="9" r="7.5"/><ellipse cx="9" cy="9" rx="3.3" ry="7.5"/><path d="M1.5 9h15"/></svg>
    ENG
    <svg width="12" height="8" viewBox="0 0 12 8"><path d="M1 1l5 5 5-5" fill="none" stroke="#666" stroke-width="1.3"/></svg>
  </div>
  <nav class="abs nav">
    <span class="active">Home</span><span>Industry Insights</span><span>Oil &amp; Gas Opportunities</span><span>Supplier &amp; Company Network</span><span>Legal Framework</span><span>News</span>
  </nav>
</header>

<section class="hero">
  <div class="hero-photo" role="img" aria-label="Offshore oil platform at sea with two engineers in hard hats reviewing a tablet"></div>
  <svg class="hero-curve" width="1200" height="170" viewBox="0 0 1200 170"><path d="M0 50 Q600 300 1200 0 L1200 170 L0 170Z" fill="#fff"/></svg>
  <h1 class="abs display">Access Mozambique’s Oil &amp;<br>Gas Industry Intelligence<br>in One Platform</h1>
  <p class="abs">Pelmarq is a modern online connection and consulting platform designed to facilitate access to the Mozambican Oil and Gas industry through premium industry insights, supplier information, tenders, legal frameworks, and strategic project data.</p>
  <a class="abs btn">Register Now</a>
  <div class="abs dots"><span></span><span class="on"></span><span></span></div>
</section>

<section class="about">
  <div class="abs about-photo" role="img" aria-label="Engineer in orange coveralls at a drilling control console"></div>
  <h2 class="abs display">What is Pelmarq?</h2>
  <div class="abs rule"></div>
  <div class="abs copy">
    <p>Pelmarq is a unique online platform built to connect businesses, investors, suppliers, and professionals with valuable information about the Mozambican Oil &amp; Gas sector.</p>
    <p>Through a secure digital paywall system, users gain access to organized, up-to-date, and carefully selected industry information that supports better decision-making, market understanding, and business opportunities within Mozambique’s growing hydrocarbons industry.</p>
  </div>
  <a class="abs btn">Read More</a>
</section>

<section class="access" aria-label="What you will access">
  <h2 class="abs display">What You Will Access</h2>
  <div class="abs rule"></div>
  <div class="abs arrow" style="left:38px"><svg width="12" height="14" viewBox="0 0 12 14"><path d="M9 1L3 7l6 6" fill="none" stroke="#1e1a3b" stroke-width="2.5"/></svg></div>
  <article class="abs card" style="left:111px">
    <div class="card-icon"><svg width="46" height="46" viewBox="0 0 46 46" fill="none" stroke="#fff" stroke-width="2.5"><path d="M12 10c-5 8-7 11-7 15a7 7 0 0014 0c0-4-2-7-7-15z"/><path d="M30 8l-6 30M30 8l6 30M26 22h8M24 32h12"/></svg></div>
    <h3>Hydrocarbon Industry<br>Information</h3>
    <p>General information and insights about Mozambique’s oil and gas sector.</p>
  </article>
  <article class="abs card card-feature" style="left:441px">
    <div class="ring" role="img" aria-label="Aerial view of a gas processing plant with storage tanks"></div>
    <h3>Main Gas Projects</h3>
  </article>
  <article class="abs card" style="left:772px">
    <div class="card-icon"><svg width="46" height="46" viewBox="0 0 46 46" fill="#fff"><circle cx="16" cy="13" r="6"/><path d="M5 36c0-7 5-12 11-12s11 5 11 12z"/><rect x="26" y="20" width="15" height="16" rx="1"/></svg></div>
    <h3>Supplier &amp; Company<br>Database</h3>
    <p>Mozambican companies capable of meeting Level 3 supply requirements.</p>
  </article>
  <div class="abs arrow" style="left:1127px"><svg width="12" height="14" viewBox="0 0 12 14"><path d="M3 1l6 6-6 6" fill="none" stroke="#1e1a3b" stroke-width="2.5"/></svg></div>
</section>

<section class="unique">
  <h2 class="abs display">Why Pelmarq is Unique</h2>
  <div class="abs rule"></div>
  <div class="abs feature" style="top:240px">
    <div class="ico"><svg width="40" height="40" viewBox="0 0 40 40" fill="none" stroke="#f0762d" stroke-width="2.5"><path d="M32 20a12 12 0 11-4-9"/><path d="M29 5v7h-7"/></svg></div>
    <div><h3>Up-to-Date Industry Intelligence</h3><p>Receive frequent updates about developments in Mozambique’s Oil &amp; Gas sector.</p></div>
  </div>
  <div class="abs feature" style="top:368px">
    <div class="ico"><svg width="40" height="40" viewBox="0 0 40 40" fill="none" stroke="#f0762d" stroke-width="2.5"><circle cx="20" cy="20" r="14" stroke-dasharray="5 3"/><circle cx="20" cy="20" r="9"/><path d="M15 20l4 4 6-7"/></svg></div>
    <div><h3>High-Quality Curated Information</h3><p>Access carefully selected and synthesized information tailored to industry stakeholders.</p></div>
  </div>
  <div class="abs feature" style="top:497px">
    <div class="ico"><svg width="40" height="40" viewBox="0 0 40 40" fill="none" stroke="#f0762d" stroke-width="2.5"><circle cx="22" cy="14" r="9"/><path d="M22 9v5h4"/><path d="M5 30h8l6 3h10l6-5"/></svg></div>
    <div><h3>Time-Saving Access</h3><p>Avoid spending hours searching through scattered online sources with organized and accessible content in one platform.</p></div>
  </div>
  <div class="abs unique-photo" role="img" aria-label="Offshore oil platform and pipeline at sunset"></div>
</section>

<section class="how">
  <svg class="abs how-photo" width="610" height="485" viewBox="0 0 610 485" role="img" aria-label="Engineer holding a tablet beside an illuminated offshore rig with a digital network overlay">
    <defs><linearGradient id="howGrad" x1="0" y1="0" x2="1" y2="1"><stop offset="0" stop-color="#0f4f6e"/><stop offset=".55" stop-color="#0b2b45"/><stop offset="1" stop-color="#8a6a2a"/></linearGradient></defs>
    <path d="M0 0H545Q640 240 540 485H0Z" fill="url(#howGrad)"/>
    <path d="M545 0Q640 240 540 485" fill="none" stroke="#fff" stroke-width="6"/>
  </svg>
  <h2 class="abs display">How the Platform Works</h2>
  <div class="abs rule"></div>
  <p class="abs">The platform operates through a secure automated payment system that grants registered users access to premium and exclusive content. By subscribing, users receive organized industry intelligence designed to save time, improve market access, and support strategic business growth within Mozambique’s energy sector.</p>
  <a class="abs btn">Read More</a>
</section>

<section class="cta">
  <h2 class="abs display">Start Exploring Mozambique’s<br>Oil &amp; Gas Opportunities</h2>
  <div class="abs rule"></div>
  <p class="abs">Register today to access premium industry information, supplier networks,<br>tenders, and strategic market insights through Pelmarq.</p>
  <div class="abs btns"><a class="btn">Register Now</a><a class="btn btn-dark">Contact Us</a></div>
</section>

<footer class="site-footer">
  <svg class="footer-bg" width="1200" height="436" viewBox="0 0 1200 436"><path d="M0 130Q600 -80 1200 130V436H0Z" fill="#1b1930"/></svg>
  <div class="abs links">
    <h4>Quick Links</h4>
    <ul><li>Home</li><li>Industry Insights</li><li>Oil &amp; Gas Opportunities</li><li>Supplier &amp; Company Network &nbsp;&nbsp;&nbsp;&nbsp;Legal Framework</li><li>News</li><li>Contact Us</li></ul>
  </div>
  <div class="abs foot-brand">
    <div class="logo-dot"></div>
    <div class="brand-name">PELMARQ CO</div>
    <div class="tagline">LINKING TALENT. DRIVING OUTCOMES.</div>
    <div class="social"><span></span><span></span><span></span></div>
  </div>
  <div class="abs contact">
    <h4>Contact Info</h4>
    <ul>
      <li><svg width="18" height="20" viewBox="0 0 18 20"><path d="M9 1a7 7 0 00-7 7c0 5 7 11 7 11s7-6 7-11a7 7 0 00-7-7z" fill="#fff"/><circle cx="9" cy="8" r="2.5" fill="#1b1930"/></svg>12 Vessel Lane Harbour Point, Coastvale South Africa</li>
      <li><svg width="18" height="18" viewBox="0 0 18 18"><circle cx="9" cy="9" r="9" fill="#fff"/><rect x="4" y="6" width="10" height="7" fill="#1b1930"/></svg>hello@pelmarqmz.org</li>
      <li><svg width="18" height="18" viewBox="0 0 18 18"><path d="M4 1l4 4-2 2c1 2 3 4 5 5l2-2 4 4-2 3C8 17 1 10 1 3z" fill="#fff"/></svg>+1 555 010 0199</li>
    </ul>
  </div>
  <div class="abs foot-line"></div>
  <div class="abs copyright">Copyrights© Pelmarq Co.All Rights Reserved</div>
  <div class="abs chat"><svg width="26" height="20" viewBox="0 0 26 20"><rect x="1" y="1" width="24" height="14" rx="7" fill="#fff"/><circle cx="8" cy="8" r="1.6" fill="#f0762d"/><circle cx="13" cy="8" r="1.6" fill="#f0762d"/><circle cx="18" cy="8" r="1.6" fill="#f0762d"/></svg></div>
</footer>

</body>
</html>
```